Business Card for Multi-Brand Sportswear Company

We are looking for a business card which represents our company and the multiple brands within it.

The company: Kelvo Athletics (LTD)
The brands: Kelv, TaliMati, VerdantFlex, Grit and Grime

Employees using these cards would be representing Kelvo Athletics, rather than any of the individual brands. You will see a current design within the uploaded files, to give some inspiration. The actual text of the brands is not necessary, but the logos should be on there is some format.

Our creative minds on this are stretched, so we are looking for someone to make this their own, and show us what a good business card should look like.

We may like to get these printed with spot gloss, so keep that in mind with your designs.

www.kelvoathletics.co.uk

Industry/Entity Type

Business

Contact Information for Business Card

Tom Pennington-Hale
Operations Manager
(+44) 1632 960 417
Tom@kelvoathletics.co.uk
www.kelvoathletics.co.uk

Font styles to use
Sans Serif
Other font styles liked:
• Eurostile

Colors
ffffff

Requirements
Nice to have
• Dark (black) background

```html
<!DOCTYPE html>
<html lang="en">
<head>
<meta charset="utf-8">
<title>Kelvo Athletics – Business Card</title>
<link rel="stylesheet" href="https://fonts.googleapis.com/css2?family=Arimo:wght@400;700&family=Saira:wght@400&display=swap">
<style>
  :root {
    --stage: #f4f4f4;
    --card: #ffffff;
    --facet-light: #fbfbfb;
    --facet-dark: #e6e6e6;
    --ink: #111111;
    --accent: #d7191f;
    --brand-grey: #9a9a9a;
    --brand-plum: #6b5670;
  }
  * { box-sizing: border-box; margin: 0; padding: 0; }
  html, body { width: 1200px; height: 586px; overflow: hidden; }
  body {
    background: var(--stage);
    position: relative;
    font-family: "Arimo", Arial, sans-serif;
    color: var(--ink);
  }
  .card {
    position: absolute;
    top: 128px;
    width: 502px;
    height: 302px;
    background: var(--card);
    overflow: hidden;
  }
  .card--front { left: 66px; }
  .card--back { left: 608px; }
  .card__texture {
    position: absolute;
    inset: 0;
    background: linear-gradient(135deg, var(--facet-light) 0%, var(--facet-dark) 45%, var(--facet-light) 70%, var(--facet-dark) 100%);
  }
  .wordmark {
    position: absolute;
    display: flex;
    align-items: center;
    font-family: "Saira", "Eurostile", sans-serif;
    font-weight: 400;
    color: var(--ink);
    white-space: nowrap;
  }
  .wordmark__square {
    background: var(--accent);
    margin-right: 12px;
  }
  .card--front .wordmark {
    left: 0; right: 0; top: 124px;
    justify-content: center;
    font-size: 40px;
    letter-spacing: 0.5px;
  }
  .card--front .wordmark__square { width: 30px; height: 30px; }
  .card--back .wordmark {
    left: 30px; top: 30px;
    font-size: 28px;
  }
  .card--back .wordmark__square { width: 22px; height: 22px; margin-right: 10px; }
  .holder {
    position: absolute;
    right: 32px;
    top: 146px;
    text-align: right;
  }
  .holder__name { font-size: 17px; font-weight: 700; }
  .holder__rule {
    position: absolute;
    left: 26px;
    top: 172px;
    width: 334px;
    height: 3px;
    background: var(--accent);
  }
  .holder__title {
    position: absolute;
    right: 32px;
    top: 166px;
    font-size: 12px;
  }
  .contacts {
    position: absolute;
    left: 30px;
    top: 188px;
    list-style: none;
    font-size: 12px;
  }
  .contacts li {
    display: flex;
    align-items: center;
    height: 24.5px;
  }
  .contacts svg { width: 14px; height: 12px; margin-right: 6px; fill: var(--accent); }
  .contacts .contacts__email { font-size: 10.5px; }
  .address {
    position: absolute;
    left: 31px;
    top: 261px;
    font-size: 12.5px;
    font-weight: 700;
  }
  .brands {
    position: absolute;
    right: 28px;
    top: 262px;
    display: flex;
    gap: 10px;
    align-items: center;
  }
  .brand-name {
    font-family: "Saira", "Eurostile", sans-serif;
    font-size: 10px;
    white-space: nowrap;
  }
  .brand-name--grey { color: var(--brand-grey); }
  .brand-name--red { color: var(--accent); }
  .brand-name--plum { color: var(--brand-plum); }
  .brand-name--ink { color: var(--ink); }
</style>
</head>
<body>

  <section class="card card--front">
    <div class="card__texture" role="img" aria-label="Faceted low-poly white and pale grey background texture"></div>
    <div class="wordmark"><span class="wordmark__square"></span>Kelvo Athletics</div>
  </section>

  <section class="card card--back">
    <div class="card__texture" role="img" aria-label="Faceted low-poly white and pale grey background texture"></div>
    <div class="wordmark"><span class="wordmark__square"></span>Kelvo Athletics</div>

    <div class="holder"><p class="holder__name">Dan Halloway</p></div>
    <div class="holder__rule"></div>
    <p class="holder__title">Managing Director</p>

    <ul class="contacts">
      <li>
        <svg viewBox="0 0 14 12" aria-hidden="true"><path d="M1 4 C1 1.5 4 1 7 1 C10 1 13 1.5 13 4 L10 4 L9.5 3 L4.5 3 L4 4 Z"/><path d="M3 5 L11 5 L12 11 L2 11 Z"/></svg>
        +44 (0)1632 960 218
      </li>
      <li>
        <svg viewBox="0 0 14 12" aria-hidden="true"><rect x="3.5" y="0.5" width="7" height="3"/><rect x="0.5" y="4" width="13" height="5" rx="1"/><rect x="3.5" y="8" width="7" height="3.5"/></svg>
        (555) 014-2287
      </li>
      <li class="contacts__email">
        <svg viewBox="0 0 14 12" aria-hidden="true"><path d="M0.5 1.5 H13.5 V10.5 H0.5 Z M1.5 2.5 L7 7 L12.5 2.5" stroke="#fff" stroke-width="0.8"/></svg>
        dan@kelvoathletics.co.uk
      </li>
    </ul>

    <p class="address">Eastfield Court, Marlow Vale, ZZ1 4QT</p>

    <div class="brands">
      <span class="brand-name brand-name--grey">TaliMati</span>
      <span class="brand-name brand-name--red">Grit and Grime</span>
      <span class="brand-name brand-name--plum">VerdantFlex</span>
      <span class="brand-name brand-name--ink">Kelv</span>
    </div>
  </section>

</body>
</html>
```